Design some Business Cards for BrightPath.

Attached please find the logo.

NO ART WORK OR PHOTOS OF THE PHONES ARE ALLOWED.

USE ONLY NATURAL (from logo) COLORS TO DESIGN THE BUSINESS CARD

Name : Tomas Weld
Phone : 404 731 2846
Toll Free : 1-888-615-9042
Fax : 1-888-615-KEMB
Email : Tomas@[url removed, login to view]
Address : 7142 Linden Crest Rd NE, Atlanta, GA 30329

```html
<!DOCTYPE html>
<html lang="en">
<head>
<meta charset="utf-8">
<title>BrightPath Business Cards</title>
<link href="https://fonts.googleapis.com/css2?family=Roboto+Condensed:wght@400;700&display=swap" rel="stylesheet">
<style>
  :root {
    --stage: #1b4f8e;
    --card-white: #f7f8f5;
    --brand-green: #8fc43f;
    --brand-blue: #2a8dd0;
    --name-teal: #2f7f95;
    --text-blue: #1f87c9;
    --faint-blue: #c9def0;
  }
  * { margin: 0; padding: 0; box-sizing: border-box; }
  html, body { width: 1200px; height: 617px; overflow: hidden; }
  body {
    background: var(--stage);
    font-family: "Roboto Condensed", "Arial Narrow", sans-serif;
    position: relative;
  }
  .card {
    position: absolute;
    top: 143px;
    width: 535px;
    height: 331px;
    overflow: hidden;
    box-shadow: 0 6px 18px rgba(0,0,0,0.3);
  }
  .card-front { left: 57px; background: var(--card-white); }
  .card-back { left: 613px; background: var(--brand-blue); }

  .front-band {
    position: absolute; left: 0; top: 0; width: 100%; height: 37px;
    background: var(--brand-green);
  }
  .holder-name {
    position: absolute; right: 16px; top: 7px;
    font-size: 22px; font-weight: 400; color: var(--name-teal);
  }
  .brand-decoration {
    position: absolute; left: -40px; top: 50px; width: 260px; height: 280px;
    border-radius: 50%;
    background: radial-gradient(circle at 50% 50%, var(--faint-blue) 0%, rgba(201,222,240,0) 70%);
  }
  .brand-mark {
    position: absolute; display: flex; align-items: center; gap: 8px;
  }
  .brand-dot { border-radius: 50%; background: var(--brand-blue); }
  .brand-name { font-weight: 700; color: var(--brand-green); line-height: 1; }
  .card-front .brand-mark { left: 247px; top: 110px; }
  .card-front .brand-dot { width: 30px; height: 30px; }
  .card-front .brand-name { font-size: 34px; }

  .contact-list { position: absolute; left: 224px; top: 178px; list-style: none; }
  .contact-item {
    display: flex; align-items: center; height: 27px;
    font-size: 15.5px; color: var(--text-blue);
  }
  .contact-icon { width: 14px; height: 14px; margin-right: 10px; flex: none; }

  .back-top {
    position: absolute; left: 0; top: 0; width: 100%; height: 168px;
    background: var(--brand-green);
  }
  .back-disc {
    position: absolute; left: 52px; top: 0; width: 314px; height: 314px;
    margin-top: 8px; border-radius: 50%; background: var(--card-white);
  }
  .card-back .brand-mark { left: 148px; top: 140px; }
  .card-back .brand-dot { width: 34px; height: 34px; }
  .card-back .brand-name { font-size: 40px; }
</style>
</head>
<body>

<section class="card card-front">
  <div class="front-band"></div>
  <p class="holder-name">Tomas Weld</p>
  <div class="brand-decoration" role="img" aria-label="Faint brand decoration area"></div>
  <div class="brand-mark">
    <span class="brand-dot"></span>
    <span class="brand-name">BrightPath</span>
  </div>
  <ul class="contact-list">
    <li class="contact-item">
      <svg class="contact-icon" viewBox="0 0 14 14"><path d="M7 1a4.5 4.5 0 0 0-4.5 4.5C2.5 9 7 13.5 7 13.5S11.5 9 11.5 5.5A4.5 4.5 0 0 0 7 1z" fill="#8fc43f"/><circle cx="7" cy="5.5" r="1.7" fill="#f7f8f5"/></svg>
      7142 Linden Crest Rd NE, Atlanta, GA 30329
    </li>
    <li class="contact-item">
      <svg class="contact-icon" viewBox="0 0 14 14"><circle cx="7" cy="7" r="7" fill="#8fc43f"/><path d="M5 3.5l1.2 2-0.8 0.9a5 5 0 0 0 2.2 2.2l0.9-0.8 2 1.2-0.6 1.4C7 10.6 3.4 7 3.6 4.1z" fill="#f7f8f5"/></svg>
      404 731 2846
    </li>
    <li class="contact-item">
      <svg class="contact-icon" viewBox="0 0 14 14"><circle cx="7" cy="7" r="7" fill="#8fc43f"/><path d="M5 3.5l1.2 2-0.8 0.9a5 5 0 0 0 2.2 2.2l0.9-0.8 2 1.2-0.6 1.4C7 10.6 3.4 7 3.6 4.1z" fill="#f7f8f5"/></svg>
      1-888-615-9042
    </li>
    <li class="contact-item">
      <svg class="contact-icon" viewBox="0 0 14 14"><circle cx="7" cy="7" r="7" fill="#8fc43f"/><path d="M5 3.5l1.2 2-0.8 0.9a5 5 0 0 0 2.2 2.2l0.9-0.8 2 1.2-0.6 1.4C7 10.6 3.4 7 3.6 4.1z" fill="#f7f8f5"/></svg>
      1-888-615-KEMB
    </li>
    <li class="contact-item">
      <svg class="contact-icon" viewBox="0 0 14 14"><rect x="0.5" y="3" width="13" height="9" fill="#8fc43f"/><path d="M1 3.5l6 4.5 6-4.5" fill="none" stroke="#f7f8f5" stroke-width="1.2"/></svg>
      Tomas@brightpathfix.com
    </li>
  </ul>
</section>

<section class="card card-back">
  <div class="back-top"></div>
  <div class="back-disc"></div>
  <div class="brand-mark">
    <span class="brand-dot"></span>
    <span class="brand-name">BrightPath</span>
  </div>
</section>

</body>
</html>
```